Willow of Meadow Uniform Label Redesign

To refine our current product label designs into one, simple, modern, crisp, general look that can be adapted to all our all Natural Skin Care and Wellness products. I am inspired by the elegant versatility of products like Lumavel Botanic Beauty or Tarn Beauty label schemes. We no longer want labels that indicate scent or ingredients. We have two primary colors that we want to maintain (#096CA3 and #DEE33F), and are willing to entertain subtle additions of others, other than black. Our labels will be printed on white or clear material. We use mainly Cosmo or Boston Round container shapes, plus flat top, smooth, round jars. Maybe a faded watermark highlight the "natural" or "beautiful" side of our products. we need to convey confidence, while remaining simple. We currently use the Advantage font. Maybe Century Gothic may work. Something similar that is easy on the eyes. Maybe vertical main text? We are willing to entertain a lot of ideas. These designs will offer ideas into our eventual Website (www.willowofmeadow-example.com) redesign.

Target Market(s)

Those who are familiar with the power of natural, plant based skin care and wellness products

Industry/Entity Type

Natural Skin Care and Wellness

Font styles to use
Sans Serif
Other font styles liked:
• Century Gothic, Advantage, or similar that is easy on the eyes

Colors
0054AA
0677BA
7BADD7
CADEEF
E8F1F8
59FF00
82FF00
B8FF75
E3FFCB
F4FFEA

Requirements
Must have
• "Clean Lines"; These colors: (#096CA3 and #DEE33F)
Nice to have
• MAYBE vertical main text or a watermark image

```html
<!DOCTYPE html>
<html lang="en">
<head>
<meta charset="utf-8">
<title>Willow of Meadow – Conditioning Facial Cleaner Labels</title>
<link rel="stylesheet" href="https://fonts.googleapis.com/css2?family=Montserrat:wght@300;400&display=swap">
<style>
  :root {
    --page: #ffffff;
    --label: #f6f6f7;
    --label-edge: #e6e6e9;
    --ink: #2b2b2e;
    --ink-soft: #55555a;
    --lime: #dee33f;
    --lime-light: #e6ea86;
    --lime-deep: #bcc42a;
    --white: #ffffff;
  }
  * { box-sizing: border-box; margin: 0; padding: 0; }
  html, body {
    width: 1138px; height: 1200px; overflow: hidden;
    background: var(--page);
    font-family: "Montserrat", sans-serif;
    font-weight: 400;
    color: var(--ink);
  }
  .labels { position: relative; width: 1138px; height: 1200px; }

  .label {
    position: absolute; top: 470px; width: 356px; height: 670px;
    background: var(--label);
    border: 1px solid var(--label-edge);
    border-radius: 40px;
  }
  .label--classic { left: 167px; }
  .label--vertical { left: 664px; }

  .centered {
    position: absolute; left: 0; width: 100%;
    text-align: center; white-space: nowrap;
  }

  /* Classic label (coordinates relative to label) */
  .classic__brand {
    top: 130px;
    font-size: 21px; letter-spacing: 1.5px; color: var(--ink);
  }
  .rule {
    position: absolute; left: 58px; width: 242px; height: 4px;
    background: linear-gradient(90deg, var(--lime), var(--lime-deep));
  }
  .rule--top { top: 187px; }
  .rule--bottom { top: 543px; }
  .classic__title {
    top: 278px;
    font-size: 19px; font-weight: 400; line-height: 30px;
    letter-spacing: 6px; color: var(--ink);
    padding-left: 6px;
  }
  .classic__dot {
    position: absolute; top: 400px; left: 136px;
    width: 86px; height: 86px; border-radius: 50%;
    background: linear-gradient(135deg, var(--lime), var(--lime-deep));
  }
  .volume { font-size: 17px; letter-spacing: 0.5px; color: var(--ink-soft); }
  .classic__volume { top: 602px; }

  /* Vertical label */
  .vertical__band {
    position: absolute; top: 36px; left: 60px;
    width: 137px; height: 517px;
    background: linear-gradient(90deg, var(--lime-light), var(--lime), var(--lime-deep));
  }
  .vertical__brand, .vertical__name {
    position: absolute; white-space: nowrap;
    writing-mode: vertical-rl; transform: rotate(180deg);
  }
  .vertical__brand {
    left: 22px; top: 30px; height: 345px;
    font-size: 31px; font-weight: 300; line-height: 1;
    color: var(--white); text-align: left;
  }
  .vertical__dot {
    position: absolute; left: 18px; top: 400px;
    width: 96px; height: 96px; border-radius: 50%; background: var(--white);
  }
  .vertical__name {
    left: 232px; top: 54px; height: 480px;
    font-size: 34px; font-weight: 400; letter-spacing: 14px; line-height: 1;
    color: var(--ink); text-align: center;
  }
  .vertical__product {
    top: 570px;
    font-size: 17px; font-weight: 400; letter-spacing: 5px; color: var(--ink);
    padding-left: 5px;
  }
  .vertical__volume { top: 602px; }
</style>
</head>
<body>
<main class="labels">
  <section class="label label--classic">
    <div class="centered classic__brand">WILLOW OF MEADOW</div>
    <div class="rule rule--top"></div>
    <h1 class="centered classic__title">CONDITIONING<br>FACIAL<br>CLEANER</h1>
    <div class="classic__dot"></div>
    <div class="rule rule--bottom"></div>
    <div class="centered volume classic__volume">8 fl. oz (238ml)</div>
  </section>

  <section class="label label--vertical">
    <div class="vertical__band">
      <div class="vertical__brand">Willow of Meadow</div>
      <div class="vertical__dot"></div>
    </div>
    <h1 class="vertical__name">CONDITIONING</h1>
    <div class="centered vertical__product">FACIAL CLEANER</div>
    <div class="centered volume vertical__volume">8 fl. oz (238ml)</div>
  </section>
</main>
</body>
</html>
```